Attraktives Etiketten-Design für Honig
Zielgruppe
Wir sind eine kleine solvira-zertifizierte Imkerei und suchen ein attraktives Ettiket für unsere erstklassigen Honige. Unsere Zielgruppe sind Menschen mit einem nachhaltig, ökologischen Bewusstsein.
Aufgabenstellung
Wir verkaufen zur Zeit vor allem Waldhonig, streben aber auch einen Blütenhonig an. Das Etikett soll daher entweder den Wald wiederspiegeln oder aber neutral sein, so dass der Schriftzug Waldhonig oder Blütenhonig jeweils eingesetzt werden kann. Wichtig ist mir der Ortszusatz 'aus dem Glottertal'.
Ein Etikett, das mir sehr gut gefällt, ist das von der Imkerei Brummelt (http://imkereibrummelt-beispiel.de/honig/). Toll wäre, wenn solche Goldelemente Eingang ins Etikett fänden. Das Verspielte finde ich auch schön. Es kann aber auch ganz gradlienig sein. Nur nicht halb-halb. Im Anhang habe ich auch das Bild einer Blumenbiene. Dieses Bild kann verwendet werden, muss aber nicht sein.
Unser Glas ist ein 400g Rundglas. (https://www.gefaesswelt-beispiel.de/gh/Sturzglas-350-ml--93.html)
Etikettengröße 133 x 60 mm, aber da sind wir offen für andere Maße.
Folgende Angaben sollen auf dem Etikett prominent erscheinen:
- Waldhonig bzw. Blütenhonig
- aus dem Glottertal
Folgende Angaben sind auserdem notwendig:
- Da wir solvira-zertifiziert sind, muss oben am Rand mittig das solvira-Label angebracht werden.
- EU-Bio-Logo mit folgender Beschriftung:
* DE-Öko-058
* Deutsche Landwirtschaft
* Solvira-Betrieb 31548
- (Inhalt) 400g
- Deutscher Bienenhonig
- Imkerei kelvo: Matthias Grunbeck, Birkenweg 47b, 79814 Glottertal, 07681/552017, www.kelvohonig-beispiel.de
- Mindestens haltbar bis: L 30. l Okt. Nov. Dez. l 2022 2023 2024 2025
Die Angaben beim Mindesthaltbarkeitsdatum muss ich über die Jahre anpassen können.
Auch das Feld 'aus dem Glottertal' sollte ich durch einen anderen Ortsnamen ersetzen können.
Der Infotext bei dem Etikett im Anhang kommt vermutlich auf ein Extraetikett an die Rückseite.
Die Homepage befindet sich derzeit noch im Aufbau.

```html
<!DOCTYPE html>
<html lang="de">
<head>
<meta charset="utf-8">
<title>Waldhonig aus dem Glottertal – Etikett</title>
<link rel="stylesheet" href="https://fonts.googleapis.com/css2?family=Kaushan+Script&family=Raleway:wght@400;500;600&display=swap">
<style>
  :root {
    --backdrop: #f5dbb2;
    --label: #ffffff;
    --ink: #2f3336;
    --gold: #d9ad2a;
    --gold-light: #f0d36a;
    --green-dark: #3f8a3a;
    --green: #5fb548;
    --green-olive: #8aa52c;
    --seal: #e8792a;
  }
  * { margin: 0; padding: 0; box-sizing: border-box; }
  html, body {
    width: 1200px; height: 800px; overflow: hidden;
    background: var(--backdrop);
  }
  .canvas { position: relative; width: 1200px; height: 800px; }
  .label {
    position: absolute; left: 100px; top: 120px;
    width: 1000px; height: 560px;
    background: var(--label);
    overflow: hidden;
    font-family: "Raleway", sans-serif;
    color: var(--ink);
  }
  .artwork { position: absolute; inset: 0; width: 100%; height: 100%; }
  .seal {
    position: absolute; left: 50%; top: 0; transform: translateX(-50%);
    display: flex; align-items: center; gap: 10px;
    padding: 12px 22px 14px;
    background: var(--label);
  }
  .seal-mark { width: 16px; height: 16px; background: var(--seal); }
  .seal-name { font-size: 30px; font-weight: 600; color: var(--ink); letter-spacing: 0.5px; }
  .title-block {
    position: absolute; left: 0; right: 0; top: 140px; text-align: center;
  }
  .product-name {
    font-family: "Kaushan Script", cursive;
    font-size: 100px; font-weight: 400; line-height: 1;
    color: var(--ink);
  }
  .origin {
    margin-top: 14px;
    font-size: 28px; font-weight: 500; letter-spacing: 1px;
    text-transform: uppercase;
  }
  .category {
    position: absolute; left: 0; right: 0; top: 326px;
    text-align: center; font-size: 24px; line-height: 1.15;
  }
  .net-weight {
    position: absolute; left: 464px; top: 496px;
    width: 56px; height: 56px;
  }
  .net-weight span {
    position: absolute; inset: 0;
    display: flex; align-items: center; justify-content: center;
    font-size: 11px; font-weight: 600; color: #fff;
  }
</style>
</head>
<body>
<main class="canvas">
  <section class="label">
    <svg class="artwork" viewBox="0 0 1000 560" aria-hidden="false">
      <defs>
        <radialGradient id="comb" cx="50%" cy="40%" r="60%">
          <stop offset="0" stop-color="var(--gold)" stop-opacity="0.75"/>
          <stop offset="1" stop-color="var(--gold-light)" stop-opacity="0.15"/>
        </radialGradient>
        <linearGradient id="forest-left" x1="0" y1="0" x2="1" y2="0">
          <stop offset="0" stop-color="var(--green-olive)"/>
          <stop offset="1" stop-color="var(--green)"/>
        </linearGradient>
        <linearGradient id="forest-right" x1="0" y1="0" x2="1" y2="0">
          <stop offset="0" stop-color="var(--green-dark)"/>
          <stop offset="1" stop-color="var(--green)"/>
        </linearGradient>
        <linearGradient id="brush" x1="0" y1="0" x2="1" y2="0">
          <stop offset="0" stop-color="var(--gold-light)" stop-opacity="0.2"/>
          <stop offset="0.25" stop-color="var(--gold)"/>
          <stop offset="1" stop-color="var(--gold-light)"/>
        </linearGradient>
      </defs>
      <g role="img" aria-label="Goldene Bienenwaben als Zierelement oben links">
        <ellipse cx="120" cy="30" rx="150" ry="95" fill="url(#comb)"/>
        <ellipse cx="150" cy="160" rx="80" ry="80" fill="url(#comb)"/>
      </g>
      <g role="img" aria-label="Goldene Bienenwaben als Zierelement oben rechts">
        <ellipse cx="720" cy="40" rx="110" ry="70" fill="url(#comb)"/>
        <ellipse cx="980" cy="70" rx="50" ry="90" fill="url(#comb)"/>
      </g>
      <rect role="img" aria-label="Goldener Pinselstrich hinter dem Schriftzug" x="240" y="175" width="510" height="62" rx="8" fill="url(#brush)"/>
      <path role="img" aria-label="Gezeichnete Tannen links im Bild" d="M0 150 L90 110 L180 270 L230 300 L300 420 L420 400 L450 560 L0 560 Z" fill="url(#forest-left)" opacity="0.85"/>
      <path role="img" aria-label="Gezeichnete Tannen rechts im Bild mit kleinem Reh" d="M550 420 L620 320 L700 290 L760 200 L860 160 L920 100 L1000 140 L1000 560 L550 560 Z" fill="url(#forest-right)" opacity="0.85"/>
    </svg>

    <div class="seal">
      <span class="seal-mark"></span>
      <span class="seal-name">solvira</span>
    </div>

    <div class="title-block">
      <h1 class="product-name">Waldhonig</h1>
      <p class="origin">Aus dem Glottertal</p>
    </div>

    <p class="category">Deutscher<br>Bienenhonig</p>

    <div class="net-weight">
      <svg viewBox="0 0 56 56" width="56" height="56" aria-hidden="true">
        <polygon points="28,2 51,15 51,41 28,54 5,41 5,15" fill="var(--ink)"/>
      </svg>
      <span>400 G</span>
    </div>
  </section>
</main>
</body>
</html>
```